Plumbing Website

Design a simple 4 page website based on our provided logo and sketches. Winning designer should be willing to upgrade as needed (for additional fee). A design that includes SEO features is a plus.
I would like to see Home, , Services, Recent Jobs (set up for pictures), Contact. I like the water dropplet back ground. Please dont put logo in a box. File attached as exaple only, I am looking for a request service now button in the middle that will have a form fill to be emailed to two different addresses,
I would like to see vibrant colors. Examples of sites I like are www.brightvalvepipeworks.com look also at www.kmt-keystonemeridianpipes.com - this site is too busy but has good seo features.
Industry/Entity Type
Plumbing
Look and feel

```html
<!DOCTYPE html>
<html lang="en">
<head>
<meta charset="utf-8">
<title>Mesa Ridge Plumbing</title>
<link rel="stylesheet" href="https://fonts.googleapis.com/css2?family=Trocchi&family=Arimo:wght@400;700&display=swap">
<style>
:root{
  --page-dark:#242424;
  --teal:#5db1ba;
  --teal-dark:#4a9ca5;
  --teal-deep:#1f5f67;
  --header:#4c9fa8;
  --cream:#f3f0ea;
  --card:#f8f7f3;
  --lower:#eeeae3;
  --ink:#2c2a27;
  --muted:#8a8884;
  --red:#e41e26;
  --orange-top:#e8735a;
  --orange-bot:#e69a3a;
  --navy:#1d5fa6;
}
*{margin:0;padding:0;box-sizing:border-box}
html,body{width:1039px;height:1200px;overflow:hidden}
body{background:var(--page-dark);font-family:"Arimo",Arial,sans-serif;position:relative}
.page{position:absolute;left:101px;top:0;width:823px;height:1200px;background:var(--cream)}
.abs{position:absolute}

/* header + hero */
.hero{left:0;top:0;width:823px;height:489px;background:radial-gradient(ellipse at 55% 50%,#6fc3cb 0%,#5db1ba 45%,#4b9ea7 100%)}
.header-band{left:0;top:0;width:823px;height:106px;background:rgba(60,140,150,.55)}
.brand{left:72px;top:30px;display:flex;align-items:center;gap:8px;font-family:"Trocchi",serif;font-size:24px;color:var(--navy);letter-spacing:1px}
.brand-dot{width:14px;height:14px;border-radius:50%;background:var(--navy)}
.blog-link{left:534px;top:23px;font-family:"Trocchi",serif;font-size:9.5px;color:#fff}
.call{left:622px;top:16px;width:167px;height:25px;background:rgba(40,110,120,.55);border-radius:3px;color:#fff;font-family:"Trocchi",serif;font-size:10.5px;display:flex;align-items:center}
.call svg{margin:0 12px 0 8px}
.nav{left:370px;top:60px;display:flex;font-family:"Trocchi",serif;font-size:9.5px;color:#fff;letter-spacing:.3px}
.nav span{padding:0 17px;border-left:1px solid rgba(255,255,255,.3)}
.nav span:first-child{border-left:none}
.nav-active{left:354px;top:106px;width:64px;height:5px;background:var(--red)}
.faucet{left:468px;top:87px;width:312px;height:381px;border-radius:40px;background:radial-gradient(ellipse at 45% 45%,#eef1f2 0%,#b8c3c6 55%,rgba(93,177,186,0) 75%)}
.tagline{left:71px;top:222px;font-family:"Trocchi",serif;font-size:23px;line-height:31px;color:#f4f4f4}
.tagline em{font-style:normal;color:#bde8ee}
.cta{left:70px;top:301px;width:236px;height:44px;border-radius:3px;background:linear-gradient(var(--orange-top),var(--orange-bot));box-shadow:0 2px 3px rgba(0,0,0,.3);color:#fff;font-family:"Trocchi",serif;font-size:11px;display:flex;align-items:center;justify-content:center}
.dots{left:399px;top:499px;display:flex;gap:5px}
.dots i{width:10px;height:10px;border-radius:50%;background:var(--teal)}
.dots i.on{background:var(--teal-deep)}

/* capabilities */
.capabilities{left:35px;top:530px;width:753px;height:403px;background:var(--card);box-shadow:0 0 3px rgba(0,0,0,.08)}
.cap-head{left:0;top:0;width:753px;height:65px;border-bottom:1px solid #e6e3dc}
.cap-title{left:0;top:20px;width:753px;text-align:center;font-family:"Trocchi",serif;font-size:22px;color:var(--ink)}
.arrow-btn{width:22px;height:22px;border-radius:50%;display:flex;align-items:center;justify-content:center}
.arrow-prev{left:37px;top:25px;background:var(--teal)}
.arrow-next{left:694px;top:23px;background:#fff;border:1px solid #ddd}
.col-rule{top:100px;width:1px;height:303px;background:#ebe8e1}
.service{top:100px;width:200px}
.thumb{width:199px;height:118px;border:2px solid #fff;box-shadow:0 0 2px rgba(0,0,0,.3)}
.service h3{font-family:"Trocchi",serif;font-weight:400;font-size:13.5px;color:var(--ink);margin-top:29px}
.service p{font-size:10.7px;line-height:18px;color:var(--muted);margin-top:18px;width:205px}
.btn{display:inline-flex;align-items:center;justify-content:center;width:56px;height:29px;border-radius:3px;color:#fff;font-size:9.5px;font-weight:700;background:var(--teal);box-shadow:0 1px 2px rgba(0,0,0,.2)}
.btn-red{background:var(--red)}
.service .btn{margin-top:22px}

/* lower */
.lower{left:0;top:945px;width:823px;height:213px;background:var(--lower);border-top:1px dashed #dcd7cd}
.lower h2{font-family:"Trocchi",serif;font-weight:400;font-size:22px;color:var(--ink)}
.services-list{left:35px;top:30px;width:200px}
.services-list ul{list-style:none;margin-top:8px}
.services-list li{font-size:10.7px;font-weight:700;color:var(--teal);height:35px;display:flex;align-items:center;border-bottom:1px solid #dcd8cf}
.services-list li:last-child{border-bottom:none}
.services-list li::before{content:"\2192";color:#333;font-size:9px;margin-right:8px}
.basics{left:277px;top:30px;width:305px}
.basics p{font-size:10.7px;line-height:18px;color:var(--muted);margin-top:12px}
.basics .btn{margin-top:13px}
.basics-photo{left:589px;top:34px;width:200px;height:150px;border:2px solid #fff;background:linear-gradient(135deg,#e9e4df,#c58d61 60%,#3b4048)}

.footer-rule{left:0;top:1158px;width:823px;height:4px;background:var(--teal)}
.footer{left:0;top:1162px;width:823px;height:32px;background:#262626;color:#fff;font-size:8.3px;display:flex;align-items:center;justify-content:center}
.bottom-strip{left:0;top:1194px;width:1039px;height:6px;background:var(--teal)}
</style>
</head>
<body>
<div class="page">
  <section class="abs hero">
    <div class="abs faucet" role="img" aria-label="Chrome water faucet with a falling drop"></div>
    <div class="abs header-band"></div>
    <div class="abs brand"><span class="brand-dot"></span>Mesa Ridge Plumbing</div>
    <a class="abs blog-link">VISIT OUR BLOG</a>
    <div class="abs call">
      <svg width="14" height="10" viewBox="0 0 14 10"><path d="M1 4c0-3 12-3 12 0v1h-3V3.5H4V5H1z M3 6h8l1 4H2z" fill="#fff"/></svg>
      Call Us : 555-210-4386
    </div>
    <nav class="abs nav"><span>HOME</span><span>ABOUT US</span><span>SERVICES</span><span>SPECIALS</span><span>CONTACTS</span></nav>
    <div class="abs nav-active"></div>
    <h1 class="abs tagline">BEST <em>WARRANTIES</em><br>IN TOWN!</h1>
    <a class="abs cta">CLICK HERE TO REQUEST SERVICE</a>
  </section>
  <div class="abs dots"><i></i><i class="on"></i><i></i></div>

  <section class="abs capabilities">
    <div class="abs cap-head"></div>
    <h2 class="abs cap-title">Our Capabilities</h2>
    <span class="abs arrow-btn arrow-prev"><svg width="6" height="8"><path d="M5 1L2 4l3 3" stroke="#fff" fill="none"/></svg></span>
    <span class="abs arrow-btn arrow-next"><svg width="6" height="8"><path d="M1 1l3 3-3 3" stroke="#333" fill="none"/></svg></span>
    <div class="abs col-rule" style="left:258px"></div>
    <div class="abs col-rule" style="left:500px"></div>
    <article class="abs service" style="left:36px">
      <div class="thumb" role="img" aria-label="Plumber in a hard hat fixing pipes under a sink" style="background:linear-gradient(120deg,#8a8278,#d9d7d3 50%,#2b62b8)"></div>
      <h3>Residential Plumbing</h3>
      <p>Lorem ipsum dolor sit amet, consectetur adipiscing elit, sed diam nonummy nih euismod tincidunt ut laoreet dolore magn aliquam erat volutpat.</p>
      <a class="btn btn-red">MORE</a>
    </article>
    <article class="abs service" style="left:278px">
      <div class="thumb" role="img" aria-label="Hands cutting a pipe in an opened wall" style="background:linear-gradient(160deg,#9b7e5a,#e6e2dc 55%,#d3b9a6)"></div>
      <h3>Commercial Plumbing</h3>
      <p>Lorem ipsum dolor sit amet, consectetur adipiscing elit, sed diam nonummy nih euismod tincidunt ut laoreet dolore magn aliquam erat volutpat.</p>
      <a class="btn">MORE</a>
    </article>
    <article class="abs service" style="left:520px">
      <div class="thumb" role="img" aria-label="Plumbing tools, pipes and fittings on blueprints" style="background:linear-gradient(120deg,#e8e8e6,#3a6fb5 45%,#c27a4a 70%,#e4e1dc)"></div>
      <h3>Service Plans</h3>
      <p>Lorem ipsum dolor sit amet, consectetur adipiscing elit, sed diam nonummy nih euismod tincidunt ut laoreet dolore magn aliquam erat volutpat.</p>
      <a class="btn">MORE</a>
    </article>
  </section>

  <section class="abs lower">
    <div class="abs services-list">
      <h2>Services List</h2>
      <ul>
        <li>Water line repair &amp; replacement</li>
        <li>Drain line repair &amp; replacement</li>
        <li>Sump pump &amp; well pump repairs</li>
        <li>Water pressure issues</li>
      </ul>
    </div>
    <div class="abs basics">
      <h2>Plumbing Basics</h2>
      <p>Lorem ipsum dolor sit amet, consectetur adipiscing elit, sed diam nonummy nih euismod tincidunt ut laoreet dolore magn aliquam erat volutpatt wisi enim ad minim veniam, quis nostrud exerci tation ullamcorper susci.</p>
      <a class="btn">MORE</a>
    </div>
    <div class="abs basics-photo" role="img" aria-label="Plumber holding a wrench on a copper pipe"></div>
  </section>

  <div class="abs footer-rule"></div>
  <footer class="abs footer">MESA RIDGE PLUMBING SERVICES (C) 2012 PRIVACY POLICY</footer>
</div>
<div class="abs bottom-strip"></div>
</body>
</html>
```